Business Card - Apex Wellness

Please use the logo / design elements and font to design a business card that is eye catching and informative. If using "Direct Primary Care" logo element, you don't have to spell it out in the text.

Dr. Brendan Halvik
Apex Wellness - Direct Primary Care
4817 Tillbrook Rd. Suite 305
Brayton Ridge, AR 72990
Phone: 555-555-0137
ApexWellnessAR.example

```html
<!DOCTYPE html>
<html lang="en">
<head>
<meta charset="utf-8">
<title>Apex Wellness Business Card</title>
<link href="https://fonts.googleapis.com/css2?family=Poppins:wght@400;500;600;700&display=swap" rel="stylesheet">
<style>
  :root {
    --backdrop: #6a6b6f;
    --navy: #0c1a3f;
    --ink: #0d1536;
    --royal: #3556a8;
    --sky: #2aa8e0;
    --white: #ffffff;
  }
  * { margin: 0; padding: 0; box-sizing: border-box; }
  html, body {
    width: 900px; height: 1200px; overflow: hidden;
    background: var(--backdrop);
    font-family: "Poppins", sans-serif;
  }
  .canvas { position: relative; width: 900px; height: 1200px; }
  .card {
    position: absolute; left: 134px; width: 632px; height: 364px;
    box-shadow: 0 10px 22px rgba(0,0,0,0.35);
  }
  .card-front { top: 210px; background: var(--navy); }
  .card-back { top: 624px; background: var(--white); }

  .front-brand {
    position: absolute; left: 0; right: 0; top: 140px;
    text-align: center; color: var(--white);
  }
  .front-brand .brand-name {
    font-size: 44px; font-weight: 500; line-height: 1; letter-spacing: -0.5px;
  }
  .tagline {
    display: flex; align-items: center; justify-content: center; gap: 12px;
    font-weight: 500; letter-spacing: 1px;
  }
  .tagline::before, .tagline::after {
    content: ""; display: block; height: 1px; background: currentColor;
  }
  .front-brand .tagline { margin-top: 6px; font-size: 13px; }
  .front-brand .tagline::before, .front-brand .tagline::after { width: 60px; }

  .back-brand {
    position: absolute; left: 0; width: 316px; top: 120px;
    text-align: center; color: var(--ink);
  }
  .brand-dot {
    width: 42px; height: 42px; border-radius: 50%;
    background: var(--royal); margin: 0 auto 16px;
  }
  .back-brand .brand-name { font-size: 34px; font-weight: 500; line-height: 1; letter-spacing: -0.5px; }
  .back-brand .tagline { margin-top: 4px; font-size: 11px; font-weight: 600; letter-spacing: 0.5px; }
  .back-brand .tagline::before, .back-brand .tagline::after { width: 46px; }

  .divider { position: absolute; left: 316px; top: 86px; width: 3px; height: 194px; }
  .divider .thin { position: absolute; left: 1px; width: 1px; background: var(--royal); }
  .divider .thin.top { top: 0; height: 30px; }
  .divider .thin.bottom { bottom: 0; height: 32px; }
  .divider .thick { position: absolute; left: 0; top: 34px; width: 3px; height: 126px; background: var(--sky); }

  .contact { position: absolute; left: 349px; top: 80px; color: var(--ink); }
  .person-name { font-size: 24px; font-weight: 500; line-height: 1.2; }
  .person-name strong { font-weight: 700; }
  .person-role { font-size: 14px; margin-top: 3px; }
  .address { margin-top: 14px; font-size: 15px; line-height: 25px; }
  .links { margin-top: 14px; list-style: none; font-size: 15px; letter-spacing: 0.8px; }
  .links li { display: flex; align-items: center; gap: 6px; height: 25px; }
  .links svg { width: 15px; height: 15px; flex: none; }
</style>
</head>
<body>
<main class="canvas">
  <section class="card card-front">
    <div class="front-brand">
      <div class="brand-name">Apex Wellness</div>
      <div class="tagline">Direct Primary Care</div>
    </div>
  </section>

  <section class="card card-back">
    <div class="back-brand">
      <div class="brand-dot"></div>
      <div class="brand-name">Apex Wellness</div>
      <div class="tagline">Direct Primary Care</div>
    </div>

    <div class="divider">
      <span class="thin top"></span>
      <span class="thick"></span>
      <span class="thin bottom"></span>
    </div>

    <div class="contact">
      <div class="person-name"><strong>Dr. Brendan</strong> Halvik</div>
      <div class="person-role">Director</div>
      <div class="address">4817 Tillbrook Rd. Suite 305<br>Brayton Ridge, AR 72990</div>
      <ul class="links">
        <li>
          <svg viewBox="0 0 24 24" aria-hidden="true"><path fill="#3556a8" d="M6.6 10.8c1.4 2.8 3.8 5.1 6.6 6.6l2.2-2.2c.3-.3.7-.4 1-.2 1.1.4 2.3.6 3.6.6.6 0 1 .4 1 1V20c0 .6-.4 1-1 1C10.6 21 3 13.4 3 4c0-.6.4-1 1-1h3.5c.6 0 1 .4 1 1 0 1.2.2 2.4.6 3.6.1.3 0 .7-.2 1z"/></svg>
          555-555-0137
        </li>
        <li>
          <svg viewBox="0 0 24 24" aria-hidden="true"><rect x="2" y="5" width="20" height="14" fill="#2aa8e0"/><path d="M2 5l10 8 10-8M2 19l7-7M22 19l-7-7" stroke="#fff" stroke-width="1.5" fill="none"/></svg>
          info@apexwellnessar.example
        </li>
        <li>
          <svg viewBox="0 0 24 24" aria-hidden="true"><g fill="none" stroke="#3556a8" stroke-width="1.8"><circle cx="12" cy="12" r="9"/><ellipse cx="12" cy="12" rx="4" ry="9"/><path d="M3 12h18M4.5 7.5h15M4.5 16.5h15"/></g></svg>
          ApexWellnessAR.example
        </li>
      </ul>
    </div>
  </section>
</main>
</body>
</html>
```